Business card design needed

I need a business card design for a dog walking, dog minding and dog training business. Please refer to my website for the basic company colours and fonts I'm after. Planning on a double sided card, so all information doesn't need to be on the 'front' side.
Cheers

Industry/Entity Type

Dog Training

Contact Information for Business Card

Meadow Paws - happy hounds
Rua 0498307164
meadowpawsdemo.com.au
-walking
-holiday stays
-onsite care
-training and behavioural consultations

```html
<!DOCTYPE html>
<html lang="en">
<head>
<meta charset="utf-8">
<title>Meadow Paws – business card</title>
<link rel="stylesheet" href="https://fonts.googleapis.com/css2?family=Cinzel:wght@700&family=Open+Sans:wght@400&display=swap">
<style>
  :root {
    --card-dark: #333333;
    --accent-orange: #c8511e;
    --paper-white: #ffffff;
    --cut-line: #111111;
    --tool-grey: #d9d9d9;
  }
  html, body {
    margin: 0;
    padding: 0;
    width: 1200px;
    height: 691px;
    overflow: hidden;
    background: var(--paper-white);
  }
  .card {
    display: block;
    width: 1200px;
    height: 691px;
  }
  .bone-cutline { fill: none; stroke: var(--cut-line); stroke-width: 36; stroke-dasharray: 7 5; }
  .bone-border { fill: none; stroke: var(--paper-white); stroke-width: 29; stroke-linejoin: round; }
  .bone-body { fill: var(--card-dark); }
  .cut-trail { stroke: var(--cut-line); stroke-width: 3; stroke-dasharray: 7 5; }
  .scissors-area { fill: var(--tool-grey); }
  .brand-name { font-family: "Cinzel", serif; font-weight: 700; font-size: 56px; fill: var(--accent-orange); }
  .brand-tagline { font-family: "Open Sans", sans-serif; font-size: 30px; fill: var(--paper-white); }
  .contact-phone { font-family: "Open Sans", sans-serif; font-size: 34px; fill: var(--accent-orange); letter-spacing: 1px; }
  .contact-web { font-family: "Open Sans", sans-serif; font-size: 34px; fill: var(--paper-white); }
  .services-list { font-family: "Open Sans", sans-serif; font-size: 24px; fill: var(--accent-orange); }
  .services-consult { font-family: "Open Sans", sans-serif; font-size: 24px; fill: var(--paper-white); }
  .icon-phone-frame { fill: none; stroke: var(--accent-orange); stroke-width: 3; }
  .icon-phone-shape { fill: var(--accent-orange); }
  .icon-web-frame { fill: none; stroke: var(--paper-white); stroke-width: 3; }
  .icon-web-line { fill: none; stroke: var(--paper-white); stroke-width: 2.5; }
</style>
</head>
<body>
<svg class="card" viewBox="0 0 1068 615" preserveAspectRatio="xMidYMid meet" xmlns="http://www.w3.org/2000/svg">
  <defs>
    <path id="bone-outline" d="M 120 40 C 200 20 280 60 320 150 C 332 178 360 190 400 190 L 690 175 C 740 172 760 130 790 95 C 830 55 920 45 990 85 C 1050 120 1060 200 1020 250 C 990 285 985 310 1010 340 C 1060 400 1050 500 990 540 C 920 580 850 560 820 500 C 800 460 770 440 720 430 L 420 400 C 370 395 340 420 320 470 C 290 550 210 585 130 570 C 60 555 30 490 50 430 C 65 390 100 360 95 320 C 90 290 55 260 45 200 C 35 130 60 55 120 40 Z"/>
  </defs>

  <g class="bone">
    <use href="#bone-outline" class="bone-cutline"/>
    <use href="#bone-outline" class="bone-border"/>
    <use href="#bone-outline" class="bone-body"/>
  </g>

  <line class="cut-trail" x1="712" y1="72" x2="792" y2="68"/>
  <rect class="scissors-area" x="558" y="4" width="150" height="128" rx="40"
        role="img" aria-label="Scissors cutting along the dashed line"/>

  <g class="contact">
    <text class="contact-phone" transform="translate(166 418) rotate(-90)">Rua 0498 307 164</text>
    <text class="contact-web" transform="translate(250 418) rotate(-90)" textLength="320" lengthAdjust="spacingAndGlyphs">meadowpawsdemo.com.au</text>

    <g class="icon-phone" transform="translate(130 443)">
      <rect class="icon-phone-frame" x="0" y="0" width="34" height="58" rx="4"/>
      <path class="icon-phone-shape" d="M 9 12 h 8 v 6 h -4 v 22 h 4 v 6 h -8 c -3 0 -4 -2 -4 -4 v -26 c 0 -2 1 -4 4 -4 z"/>
      <rect class="icon-phone-shape" x="20" y="25" width="6" height="8" rx="1"/>
    </g>

    <g class="icon-web" transform="translate(207 440)">
      <rect class="icon-web-frame" x="0" y="0" width="58" height="58" rx="4"/>
      <circle class="icon-web-line" cx="29" cy="29" r="17"/>
      <ellipse class="icon-web-line" cx="29" cy="29" rx="7" ry="17"/>
      <line class="icon-web-line" x1="12" y1="29" x2="46" y2="29"/>
    </g>
  </g>

  <g class="brand" transform="rotate(-5 530 290)">
    <text class="brand-name" x="330" y="300" textLength="410" lengthAdjust="spacingAndGlyphs">MEADOW PAWS</text>
    <text class="brand-tagline" x="390" y="350">happy hounds</text>
  </g>

  <g class="services">
    <text class="services-list" transform="translate(887 548) rotate(-90)" textLength="460" lengthAdjust="spacingAndGlyphs">Walking * Holiday stays * Onsite care</text>
    <text class="services-consult" transform="translate(922 562) rotate(-90)" textLength="492" lengthAdjust="spacingAndGlyphs">Training and behavioural consultations</text>
  </g>
</svg>
</body>
</html>
```